Tidal Fern Business Cards

We need something new, fun and exciting for business cards. Our current ones are just plain and we need a design that pops. We want name, position held, phone, email on the front, and a 20% discount on the back. I have also uploaded our old business cards creative to see what we are not wanting, and how boring they were and we want something jazzed up from this, cool design and catches people attention.

```html
<!DOCTYPE html>
<html lang="en">
<head>
<meta charset="UTF-8">
<title>Tidal Fern Business Cards</title>
<link rel="stylesheet" href="https://fonts.googleapis.com/css2?family=Outfit:wght@200;300;400;500;700;800&display=swap">
<style>
  :root {
    --backdrop: #f14d4d;
    --navy: #1d3f75;
    --navy-ink: #14285a;
    --coral: #f26e6c;
    --coral-deep: #d9383c;
    --paper: #f6f5f3;
    --white: #ffffff;
  }
  * { box-sizing: border-box; margin: 0; padding: 0; }
  html, body {
    width: 1200px;
    height: 1000px;
    overflow: hidden;
  }
  body {
    background: var(--backdrop);
    font-family: "Outfit", sans-serif;
    display: flex;
    align-items: center;
    justify-content: center;
    gap: 40px;
  }
  .card {
    position: relative;
    width: 540px;
    height: 310px;
    border-radius: 4px;
    overflow: hidden;
    box-shadow: 0 24px 50px rgba(120, 10, 10, 0.3);
  }

  /* Front */
  .card-front {
    background: var(--navy);
    color: var(--white);
  }
  .card-front .accent-disc {
    position: absolute;
    right: -110px;
    top: -60px;
    width: 300px;
    height: 300px;
    border-radius: 50%;
    background: var(--coral);
  }
  .identity {
    position: absolute;
    left: 36px;
    top: 112px;
    display: flex;
    align-items: center;
    gap: 14px;
  }
  .identity .marker {
    width: 24px;
    height: 24px;
    border-radius: 50%;
    background: var(--coral);
    flex: none;
  }
  .person-name {
    font-size: 36px;
    line-height: 1;
    letter-spacing: -0.5px;
    font-weight: normal;
  }
  .person-name .first { font-weight: 800; }
  .person-name .last { font-weight: 200; }
  .person-role {
    position: absolute;
    left: 74px;
    top: 158px;
    font-size: 13px;
    font-weight: 500;
    letter-spacing: 3px;
    text-transform: uppercase;
    color: var(--coral);
  }
  .contact-list {
    position: absolute;
    left: 74px;
    bottom: 32px;
    list-style: none;
    font-size: 16px;
    font-weight: 500;
    line-height: 1.35;
    letter-spacing: 0.6px;
  }

  /* Back */
  .card-back {
    background: var(--paper);
    display: flex;
    flex-direction: column;
    align-items: center;
    justify-content: center;
  }
  .brand-lockup {
    display: flex;
    align-items: center;
    gap: 18px;
  }
  .brand-lockup .marker {
    width: 34px;
    height: 34px;
    border-radius: 50%;
    background: var(--coral-deep);
  }
  .brand-name {
    font-size: 58px;
    font-weight: 700;
    color: var(--navy-ink);
    letter-spacing: -1px;
    line-height: 1;
  }
  .offer {
    margin-top: 30px;
    margin-left: 52px;
    font-size: 20px;
    font-weight: 300;
    letter-spacing: 3px;
    color: var(--coral);
  }
</style>
</head>
<body>
  <section class="card card-front" aria-label="Business card front">
    <div class="accent-disc"></div>
    <div class="identity">
      <span class="marker"></span>
      <h1 class="person-name"><span class="first">Renato</span> <span class="last">Valez</span></h1>
    </div>
    <p class="person-role">Sales Director</p>
    <ul class="contact-list">
      <li>E: r.valez@tidalfern.com</li>
      <li>C: (044) 55 3907-2164</li>
      <li>O: (55) 5182-4470</li>
    </ul>
  </section>

  <section class="card card-back" aria-label="Business card back">
    <div class="brand-lockup">
      <span class="marker"></span>
      <span class="brand-name">Tidal Fern</span>
    </div>
    <p class="offer">20% DISCOUNT</p>
  </section>
</body>
</html>
```